- Please see our description here:
http://zestova.example/lorin/blog/zestova-player-v1

- Zestova Player needs to "look & feel" like a HTML 5 Web application.

- All of the additional pages and Zestova elements that the user goes to, need to fit within the player interface. So for example, when the user clicks on the profile it will pull it into the player as apposed to opening a new page.

- For further instructions, please send me a private message to http://zestova.example/lorin and we will send you our site work flow chart interface examples.

I just added 2 mockups that I want you guys to look at carefully and understand what we are trying to do:

http://zestova.example/media/files/public/blog/image-4-1564_2.jpg
http://zestova.example/media/files/public/blog/image-4-1564_4.jpg

the idea is that everything is controlled from the new menu button (the nice purple one).
it will throw an overlay with all our navigational choices.
and those icons will be displayed.
with this approach, we can get to everywhere in our site with no more then 2 clicks.
right from the zestova player.
if the users profile pic is clicked, we pull in the profile in an overlay as well.
we almost never leave the player.

can we do it or what?

Lorin

Target Market(s)

Social Foodies, Food Lovers, Pro and Amateur Chefs, House wives and husbands, Recipe lovers, and more

Industry/Entity Type

Media

Requirements
Must have
• We are staying on the same page as user selects options from the menu. Must have an application feel.

Try logging in to our current site and look around, to see partial example of what we are talking about. (www.zestova.example)

The site should feature a friendly chef, a character that offers pop-up tips on how to use features of the site.

In the top right corner of the site we need a common menu that takes user to a dashboard popup from which she can do most common activities on the site (create, share, search, suggest, compete, my profile)

```html
<!DOCTYPE html>
<html lang="en">
<head>
<meta charset="utf-8">
<title>Zestova – Create. Compete. Enjoy.</title>
<link rel="stylesheet" href="https://fonts.googleapis.com/css2?family=Delius&family=Lato:wght@400;700&display=swap">
<style>
:root{
  --page:#000000;
  --panel:#eeebeb;
  --orange:#e8612c;
  --orange-deep:#c9501b;
  --green:#7d9a2c;
  --ink:#1d1d1d;
  --muted:#8a8a8a;
  --white:#ffffff;
  --bar-top:#4a4a4a;
  --bar-bottom:#151515;
  --gold:#f6b73a;
  --link-blue:#3b5b9a;
  --sky:#38a9dc;
}
*{box-sizing:border-box;margin:0;padding:0}
html,body{width:786px;height:1200px;overflow:hidden;background:var(--page)}
body{position:relative;font-family:"Lato",sans-serif;color:var(--ink)}
.abs{position:absolute}

/* hero */
.hero-photo{left:0;top:0;width:786px;height:250px;
  background:linear-gradient(90deg,#c5622b 0%,#a0441b 22%,#3a1c12 45%,#5a2a1e 60%,#1b0f0c 80%,#000 100%)}
.mascot{left:45px;top:85px;width:130px;height:98px;border-radius:50%;
  background:radial-gradient(circle,#f48a34 0%,#e06a1f 55%,rgba(224,106,31,0) 72%)}
.brand{left:40px;top:184px;width:136px;text-align:center;font-family:"Delius",cursive;font-size:24px;color:var(--white)}
.tagline{left:45px;top:219px;font-family:"Delius",cursive;font-size:10px;color:#2a1208}
.chef-photo{left:615px;top:82px;width:122px;height:134px;border-radius:6px;
  background:linear-gradient(180deg,#2a2a2a,#cfcfcf 40%,#f1f1f1)}

/* top navigation */
.topbar{left:30px;top:10px;width:726px;height:34px;border-radius:7px;
  background:linear-gradient(var(--bar-top),var(--bar-bottom));box-shadow:0 1px 2px #000}
.topnav a{position:absolute;top:18px;font-family:"Delius",cursive;font-size:14px;color:var(--white);text-decoration:none}
.search{left:581px;top:17px;width:110px;height:20px;border-radius:10px;background:var(--white);
  font-size:10px;color:var(--muted);padding:4px 10px}
.social{width:18px;height:18px;border-radius:50%}
.social.a{background:var(--link-blue)}
.social.b{background:var(--sky)}

.create-btn{top:54px;width:167px;height:24px;border-radius:5px;
  background:linear-gradient(#5a5a5a,#1c1c1c);border:1px solid #777;
  font-family:"Delius",cursive;font-size:12px;color:var(--white);text-align:center;line-height:22px}
.create-btn em{font-style:normal;color:var(--gold)}
.quickmenu a{position:absolute;top:56px;font-family:"Delius",cursive;font-size:12.5px;color:var(--white);text-decoration:none}

.howto{left:609px;top:214px;width:150px;height:62px;border-radius:8px;
  background:linear-gradient(var(--orange),var(--orange-deep));border:1px solid #f28a4e}
.howto p{position:absolute;left:0;width:106px;text-align:center;font-family:"Delius",cursive;color:var(--white);font-size:12px;line-height:14px}
.howto .click{left:26px;top:41px;width:54px;height:14px;border-radius:7px;background:var(--white);color:var(--ink);font-size:10px;line-height:14px;text-align:center;position:absolute;font-weight:700}
.helper{left:94px;top:4px;width:48px;height:52px;border-radius:6px;background:linear-gradient(#6aa9d6,#2f6f9e)}

/* content */
.panel{left:33px;top:250px;width:723px;height:835px;background:var(--panel)}
.section-title{font-family:"Delius",cursive;font-size:19px;color:var(--orange);text-transform:uppercase;letter-spacing:.3px}
.about{left:52px;top:320px;width:260px;font-size:10px;line-height:18.8px}

.cuisines{left:43px;top:495px;width:270px;height:159px;border-radius:7px;
  background:linear-gradient(#1a1a1a,#3c3c3c 55%,#111);border:1px solid #555}
.cuisines ul{list-style:none}
.cuisines li{position:absolute;font-size:10.5px;color:var(--white);padding-left:11px}
.cuisines li::before{content:"";position:absolute;left:0;top:4px;width:5px;height:5px;border-radius:50%;background:var(--gold)}

.recipe-thumb{width:59px;height:57px;border:3px solid var(--white);box-shadow:0 0 3px #555;
  background:linear-gradient(135deg,#9bc24b,#d8452e 50%,#f3d37a)}
.recipe-text{width:162px;font-size:10px;line-height:12px}
.recipe-meta{font-size:9.6px;margin-top:3px;white-space:nowrap}
.recipe-meta .name{color:var(--orange)}
.recipe-meta .by{color:var(--muted);margin-left:14px}

.friends{left:57px;top:893px;width:220px;height:172px;background:var(--white);font-size:8.5px;color:#333}
.friend{position:absolute;width:47px;text-align:center}
.friend i{display:block;height:45px;background:linear-gradient(#c9c3c0,#7d7673)}
.friend span{display:block;margin-top:5px;font-size:8.4px;color:#555}
.plugin{position:absolute;left:5px;top:155px;font-size:8.5px;color:#555;padding-left:16px}
.plugin::before{content:"";position:absolute;left:0;top:0;width:12px;height:12px;background:var(--link-blue)}

.tabs .pill{left:367px;top:279px;width:78px;height:19px;border-radius:9px;background:linear-gradient(#9a9a9a,#5c5c5c);
  color:var(--white);font-family:"Delius",cursive;font-size:10px;text-align:center;line-height:19px}
.tabs .tab{top:283px;font-family:"Delius",cursive;font-size:11px;color:var(--ink)}

.post-title{left:335px;font-family:"Delius",cursive;font-size:15px;color:var(--green);text-transform:uppercase;letter-spacing:.2px}
.post-photo{left:335px;width:395px;height:233px}
.post-photo.one{background:linear-gradient(160deg,#f2f0ee,#d9cfc6 40%,#a85a2c 60%,#e9e4df)}
.post-photo.two{background:radial-gradient(ellipse at 45% 55%,#c57a2a,#8a4a1f 35%,#ece7e4 70%)}
.date{width:50px;height:50px;border-radius:50%;background:radial-gradient(#ffffff,#e8e6e6);box-shadow:0 0 3px #aaa;
  text-align:center;color:var(--orange);font-family:"Delius",cursive}
.date b{display:block;font-size:17px;font-weight:400;margin-top:7px;line-height:17px}
.date small{font-size:9px}
.byline{left:335px;font-size:9.6px}
.post-body{left:336px;width:392px;font-size:9.6px;line-height:12.3px}

.pager{left:623px;top:1042px;font-size:8px}
.pager span{display:inline-block;width:16px;height:14px;border-radius:7px;background:linear-gradient(#f3f3f3,#bdbdbd);
  border:1px solid #888;text-align:center;line-height:12px;margin-right:2px}

/* footer */
.footer a{position:absolute;top:1117px;font-family:"Delius",cursive;font-size:12px;color:var(--white);text-decoration:none;white-space:nowrap}
.copyright{left:0;width:758px;top:1151px;text-align:center;font-size:8.5px;color:#d8d8d8}
</style>
</head>
<body>

<div class="abs hero-photo" role="img" aria-label="Close-up photo of a grilled roast on a dark plate"></div>
<div class="abs mascot" role="img" aria-label="Smiling sun mascot illustration"></div>
<div class="abs brand">Zestova</div>
<div class="abs tagline">Create. Compete. Enjoy.</div>
<div class="abs chef-photo" role="img" aria-label="Photo of a friendly chef holding a plated dish"></div>

<header>
  <div class="abs topbar"></div>
  <svg class="abs" style="left:46px;top:17px" width="19" height="17" viewBox="0 0 19 17" aria-label="Home">
    <path d="M9.5 1 L18 8.5 H15.5 V16 H11.5 V11 H7.5 V16 H3.5 V8.5 H1 Z" fill="#fff"/>
  </svg>
  <nav class="topnav">
    <a style="left:92px" href="#">Profile</a>
    <a style="left:157px" href="#">Tornaments</a>
    <a style="left:258px" href="#">Chefs</a>
    <a style="left:325px" href="#">Help</a>
    <a style="left:380px" href="#">Login / Register</a>
  </nav>
  <div class="abs search">Search</div>
  <svg class="abs" style="left:672px;top:18px" width="17" height="17" viewBox="0 0 17 17" aria-hidden="true">
    <circle cx="7" cy="7" r="5" fill="none" stroke="#222" stroke-width="2"/><line x1="10.5" y1="10.5" x2="15.5" y2="15.5" stroke="#222" stroke-width="3"/>
  </svg>
  <div class="abs social a" style="left:699px;top:17px" aria-label="Linkly"></div>
  <div class="abs social b" style="left:722px;top:17px" aria-label="Chirpr"></div>

  <div class="abs create-btn" style="left:30px">Create <em>Tournament</em></div>
  <div class="abs create-btn" style="left:203px">Create <em>Munchie</em></div>
  <nav class="quickmenu">
    <a style="left:436px" href="#">Create</a>
    <a style="left:492px" href="#">Share</a>
    <a style="left:550px" href="#">Suggest</a>
    <a style="left:625px" href="#">Compete</a>
    <a style="left:697px" href="#">My profile</a>
  </nav>
</header>

<main>
  <div class="abs panel"></div>

  <div class="abs howto">
    <p style="top:6px">How to use<br>Our Site</p>
    <div class="click">Click me</div>
    <div class="abs helper" role="img" aria-label="Illustrated helper character with a question mark"></div>
  </div>

  <h2 class="abs section-title" style="left:52px;top:286px">About Us</h2>
  <p class="abs about">There are many variations of passages of Lorem Ipsum available, but the majority have suffered alteration in some form, by injected humour, or randomised words which don't look even slightly believable. If you are going to use a passage of Lorem Ipsum, you need to be sure there isn't anything embarrassing hidden in the middle of text. All the Lorem Ipsum generators on the Internet tend to repeat predefined chunks as necessary, making this the first true generator on the Internet</p>

  <section class="abs cuisines">
    <h2 class="abs section-title" style="left:6px;top:10px">Cuisines</h2>
    <ul>
      <li style="left:19px;top:47px">Chinese</li><li style="left:139px;top:48px">Chinese</li>
      <li style="left:19px;top:74px">Indian</li><li style="left:139px;top:75px">Indian</li>
      <li style="left:19px;top:100px">Italian</li><li style="left:139px;top:101px">Italian</li>
      <li style="left:19px;top:127px">Continental</li><li style="left:139px;top:127px">Continental</li>
    </ul>
  </section>

  <h2 class="abs section-title" style="left:55px;top:676px">Special Recipe</h2>
  <div class="abs recipe-thumb" style="left:52px;top:711px" role="img" aria-label="Photo of a colourful salad"></div>
  <div class="abs recipe-text" style="left:124px;top:715px">Lorem Ipsum is simply dummy text of the printing and typesetting industry.
    <div class="recipe-meta"><span class="name">Recipe Name</span><span class="by">Prepared by :jhone</span></div></div>
  <div class="abs recipe-thumb" style="left:52px;top:786px" role="img" aria-label="Photo of a colourful salad"></div>
  <div class="abs recipe-text" style="left:125px;top:791px">Lorem Ipsum is simply dummy text of the printing and typesetting industry.
    <div class="recipe-meta"><span class="name">Recipe Name</span><span class="by">Prepared by :jhone</span></div></div>

  <h2 class="abs section-title" style="left:55px;top:864px">Friends</h2>
  <div class="abs friends">
    <div class="abs" style="left:5px;top:5px">62580 people like <b>Zestova</b></div>
    <div class="friend" style="left:6px;top:20px"><i role="img" aria-label="Friend photo"></i><span>Marelle</span></div>
    <div class="friend" style="left:57px;top:20px"><i role="img" aria-label="Friend photo"></i><span>Tamsin</span></div>
    <div class="friend" style="left:107px;top:20px"><i role="img" aria-label="Friend photo"></i><span>Gerrit</span></div>
    <div class="friend" style="left:157px;top:20px"><i role="img" aria-label="Friend photo"></i><span>Idris</span></div>
    <div class="friend" style="left:6px;top:89px"><i role="img" aria-label="Friend photo"></i><span>Jessamyn</span></div>
    <div class="friend" style="left:57px;top:89px"><i role="img" aria-label="Friend photo"></i><span>Philippa</span></div>
    <div class="friend" style="left:107px;top:89px"><i role="img" aria-label="Friend photo"></i><span>Corinne</span></div>
    <div class="friend" style="left:157px;top:89px"><i role="img" aria-label="Friend photo"></i><span>Wilma</span></div>
    <div class="plugin">Linkly social plugin</div>
  </div>

  <div class="tabs">
    <div class="abs pill">SUGGESTED</div>
    <svg class="abs" style="left:398px;top:297px" width="12" height="7" aria-hidden="true"><path d="M0 0 H12 L6 7 Z" fill="#5c5c5c"/></svg>
    <div class="abs tab" style="left:522px">POPULAR</div>
    <div class="abs tab" style="left:670px">NEW</div>
  </div>

  <article>
    <h3 class="abs post-title" style="top:326px">Lorem Ipsum is simply dummy text</h3>
    <div class="abs post-photo one" style="top:352px" role="img" aria-label="Photo of pan-fried fish over tagliatelle with tomatoes"></div>
    <div class="abs date" style="left:680px;top:556px"><b>02</b><small>Nov 11</small></div>
    <p class="abs byline" style="top:594px">Prepared by : Arun Desai</p>
    <p class="abs post-body" style="top:613px">It is a long established fact that a reader will be distracted by the readable content of a page when looking at its layout. The point of using Lorem Ipsum Content here, content here', making it look like readable English. Many desktop and a search for 'lorem ipsum' will uncover many web sites still in their infancy. Various versions have evolved over the years, sometimes by accident</p>
  </article>

  <article>
    <h3 class="abs post-title" style="top:688px">Lorem Ipsum is simply dummy text</h3>
    <div class="abs post-photo two" style="top:715px" role="img" aria-label="Photo of seared fish with a fennel salad in orange sauce"></div>
    <div class="abs date" style="left:680px;top:918px"><b>02</b><small>Nov 11</small></div>
    <p class="abs byline" style="top:956px">Prepared by : Arun Desai</p>
    <p class="abs post-body" style="top:976px">It is a long established fact that a reader will be distracted by the readable content of a page when looking at its layout. The point of using Lorem Ipsum Content here, content here', making it look like readable English. Many desktop and a search for 'lorem ipsum' will uncover many web sites still in their infancy. Various versions have evolved over the years, sometimes by accident</p>
  </article>

  <div class="abs pager"><span>1</span><span>2</span><span>3</span>.......<span style="margin-left:3px">10</span></div>
</main>

<footer class="footer">
  <a style="left:96px" href="#">Home</a>
  <a style="left:151px" href="#">Help</a>
  <a style="left:200px" href="#">About</a>
  <a style="left:256px" href="#">Support</a>
  <a style="left:321px" href="#">Jobs</a>
  <a style="left:370px" href="#">Investors</a>
  <a style="left:442px" href="#">Contact</a>
  <a style="left:506px" href="#">Privacy Policy</a>
  <a style="left:601px" href="#">Terms of Service</a>
  <p class="abs copyright">Copyright © 2011. www.zestova.example</p>
  <div class="abs social a" style="left:642px;top:1149px" aria-label="Linkly"></div>
  <div class="abs social b" style="left:666px;top:1149px" aria-label="Chirpr"></div>
</footer>

</body>
</html>
```